Q-Rolls Business Card

We are a modern retail clothing store. Established in 1994. I need a presentable card that will amaze vendors when given to them.

Front: Logo in middle
Info Side:

Name: Tomas Velder
Cell: 630-812-4463
Work: 630-917-3384 EXT. 417
Email: Tomas@q-rolls-example.com
Website: www.Q-rolls-example.com

Industry/Entity Type

Business

```html
<!DOCTYPE html>
<html lang="en">
<head>
<meta charset="utf-8">
<title>Q-Rolls Business Card</title>
<link rel="stylesheet" href="https://fonts.googleapis.com/css2?family=Play:wght@400;700&display=swap">
<style>
  :root {
    --backdrop: #d9d9d9;
    --card: #ffffff;
    --ink: #111111;
    --label: #6f6f6f;
    --name-fill: #000000;
    --name-text: #ffffff;
  }
  * { margin: 0; padding: 0; box-sizing: border-box; }
  html, body {
    width: 1200px;
    height: 800px;
    overflow: hidden;
    background: var(--backdrop);
    font-family: "Play", sans-serif;
  }
  .stage {
    width: 1200px;
    height: 800px;
    display: flex;
    align-items: center;
    justify-content: center;
    gap: 60px;
  }
  .card {
    width: 520px;
    height: 297px;
    background: var(--card);
    box-shadow: 0 6px 18px rgba(0, 0, 0, 0.12);
    position: relative;
  }
  .card--info { order: 1; }
  .card--brand {
    order: 2;
    display: flex;
    align-items: center;
    justify-content: center;
  }
  .brand-name {
    font-weight: 700;
    font-size: 64px;
    letter-spacing: 2px;
    color: var(--ink);
    text-transform: uppercase;
  }
  .name-tag {
    position: absolute;
    left: 226px;
    top: 104px;
    background: var(--name-fill);
    color: var(--name-text);
    font-weight: 700;
    font-size: 18px;
    letter-spacing: 1.5px;
    padding: 5px 22px;
  }
  .contact-list {
    position: absolute;
    left: 80px;
    top: 150px;
    display: grid;
    grid-template-columns: 100px auto;
    column-gap: 8px;
    row-gap: 3px;
    font-size: 14px;
    line-height: 18px;
  }
  .contact-list dt {
    text-align: right;
    color: var(--label);
  }
  .contact-list dd {
    color: var(--ink);
    letter-spacing: 0.5px;
  }
</style>
</head>
<body>
  <main class="stage">
    <section class="card card--brand" aria-label="Card front">
      <span class="brand-name">Q-Rolls</span>
    </section>
    <section class="card card--info" aria-label="Card back">
      <div class="name-tag">Tomas Velder</div>
      <dl class="contact-list">
        <dt>Cell:</dt><dd>630-812-4463</dd>
        <dt>Work:</dt><dd>630-917-3384 EXT. 417</dd>
        <dt>Email:</dt><dd>Tomas@q-rolls-example.com</dd>
        <dt>Website:</dt><dd>www.Q-rolls-example.com</dd>
      </dl>
    </section>
  </main>
</body>
</html>
```